Brochure for Custom Cabinets Manufacturing Company

We need a design for the brochure for company that is doing high end cabinets for homes. The following information may be included:

Custom made Kitchens and Cabinets Company, located in Calgary.

Why us:

Availability. All kitchens are manufactured in a wide range of prices. Searching for a suitable option is easy and fun.

High quality. Our company tends to European standards. This involves the careful selection of raw materials, hardware, as well as a neat assembly.
High quality of our product is achieved through the use of modern equipment and advanced technology.

Wide selection. Selling our product includes hundreds of different options: in styles, materials, designs, and colors. All products are easy to use, functional and custom made design.

Happy Clients. We are taking into account all the wishes of our customers. We also provide warranty and customer service to bring positive emotions to our clients.

Proudly Canadian made. Calgary based production of our products. Custom orders without delays.

Superior health and safety standards.

```html
<!DOCTYPE html>
<html lang="en">
<head>
<meta charset="utf-8">
<title>Hearthline Brochure – Front and Back</title>
<link href="https://fonts.googleapis.com/css2?family=Arimo:wght@400;700&family=Open+Sans:wght@400;600;700&family=Great+Vibes&display=swap" rel="stylesheet">
<style>
  :root {
    --stage: #1f1f1f;
    --label: #ffffff;
    --green: #5cb947;
    --green-deep: #3c9a34;
    --blue: #2469c0;
    --blue-deep: #1b3f9a;
    --title-blue: #2a7bc4;
    --ink: #111111;
    --body: #444444;
    --white: #ffffff;
  }
  * { box-sizing: border-box; margin: 0; padding: 0; }
  html, body { width: 1068px; height: 1200px; overflow: hidden; background: var(--stage); }
  .stage { position: relative; width: 1068px; height: 1200px; }

  .side-label {
    position: absolute; color: var(--label);
    font-family: "Open Sans", sans-serif; font-size: 36px; font-weight: 400;
  }
  .side-label--front { left: 870px; top: 286px; }
  .side-label--back { left: 876px; top: 858px; }

  .panel { position: absolute; overflow: hidden; }
  .panel > svg.panel-art { position: absolute; inset: 0; }
  .panel > .layer { position: absolute; }

  /* front */
  .cover-back { left: 20px; top: 36px; width: 383px; height: 542px; }
  .cover-front { left: 403px; top: 36px; width: 384px; height: 542px; background: var(--white); }
  .tagline { font-family: "Great Vibes", cursive; font-size: 19px; white-space: nowrap; }
  .cover-back .tagline { left: 0; width: 100%; top: 44px; text-align: center; color: var(--white); }
  .cover-front .tagline { left: 17px; top: 50px; color: var(--green-deep); }

  .brand { font-family: "Open Sans", sans-serif; font-weight: 600; letter-spacing: -0.5px; white-space: nowrap; }
  .brand-square { position: absolute; border-radius: 4px; }
  .cover-back .brand-square { left: 150px; top: 150px; width: 84px; height: 84px; border: 5px solid var(--white); }
  .cover-back .brand { left: 0; width: 100%; top: 236px; text-align: center; color: var(--white); font-size: 28px; }
  .cover-front .brand-square { left: 242px; top: 17px; width: 84px; height: 84px; border: 5px solid var(--green); }
  .cover-front .brand { right: 20px; top: 106px; color: var(--title-blue); font-size: 28px; }

  .contact {
    left: 0; width: 100%; top: 402px; text-align: center; color: var(--white);
    font-family: "Open Sans", sans-serif; font-size: 10.5px; line-height: 15px;
  }
  .contact .gap { margin-top: 10px; }

  .cover-phone {
    right: 22px; top: 468px; color: var(--white);
    font-family: "Open Sans", sans-serif; font-weight: 700; font-size: 20px;
  }
  .cover-caption {
    right: 10px; top: 516px; color: var(--white); white-space: nowrap;
    font-family: "Open Sans", sans-serif; font-weight: 700; font-size: 10px; text-transform: uppercase;
  }

  /* back */
  .inside-left { left: 20px; top: 622px; width: 384px; height: 543px; background: var(--white); }
  .inside-right { left: 404px; top: 622px; width: 386px; height: 543px; background: var(--white); }

  .section-title {
    left: 16px; top: 164px; color: var(--ink);
    font-family: "Arimo", sans-serif; font-weight: 700; font-size: 18px;
  }
  .feature-title {
    position: absolute; color: var(--title-blue);
    font-family: "Arimo", sans-serif; font-weight: 700; font-size: 13.5px;
  }
  .inside-right .feature-title { font-weight: 400; }
  .feature-text {
    position: absolute; color: var(--body);
    font-family: "Arimo", sans-serif; font-size: 10.5px; line-height: 13px;
  }
  .inside-left .feature-title, .inside-left .feature-text { left: 64px; }
  .inside-left .feature-text { width: 300px; }
  .inside-right .feature-title, .inside-right .feature-text { left: 62px; }
  .inside-right .feature-text { width: 312px; }

  .footer-domain {
    left: 10px; top: 513px; color: var(--white);
    font-family: "Open Sans", sans-serif; font-weight: 600; font-size: 13px;
  }
  .footer-phone {
    right: 16px; top: 506px; color: var(--white);
    font-family: "Open Sans", sans-serif; font-weight: 600; font-size: 20px;
  }

  .trust-title {
    left: 17px; top: 280px; color: var(--white);
    font-family: "Arimo", sans-serif; font-weight: 700; font-size: 13px;
  }
  .trust-text {
    left: 17px; top: 305px; width: 356px; color: var(--white);
    font-family: "Arimo", sans-serif; font-size: 10.5px; line-height: 13px;
  }
</style>
</head>
<body>
<main class="stage">

  <section class="panel cover-back">
    <svg class="panel-art" viewBox="0 0 383 542" width="383" height="542" aria-hidden="true">
      <defs>
        <linearGradient id="coverGreen" x1="0" y1="0" x2="1" y2="1">
          <stop offset="0" stop-color="#6cc24a"/><stop offset="1" stop-color="#3f9c36"/>
        </linearGradient>
        <linearGradient id="coverBlue" x1="0" y1="0" x2="0" y2="1">
          <stop offset="0" stop-color="#2a78cc"/><stop offset="1" stop-color="#1b3f9a"/>
        </linearGradient>
      </defs>
      <rect width="383" height="542" fill="url(#coverGreen)"/>
      <path d="M0,312 C110,286 250,296 383,360 L383,542 L0,542 Z" fill="#ffffff"/>
      <path d="M0,324 C110,298 250,308 383,374 L383,542 L0,542 Z" fill="url(#coverBlue)"/>
    </svg>
    <p class="layer tagline">Some Tag Line Goes Here</p>
    <span class="brand-square"></span>
    <p class="layer brand">Hearthline</p>
    <address class="layer contact" style="font-style:normal">
      <p>2418 Linden Crescent</p>
      <p>Calgary, AB T2N 4K7</p>
      <p class="gap">Ph: 1 888 402 5176</p>
      <p class="gap">Mail: hello@hearthlinekitchens.com</p>
      <p class="gap">www.hearthlinekitchens.com</p>
    </address>
  </section>

  <section class="panel cover-front">
    <svg class="panel-art" viewBox="0 0 384 542" width="384" height="542">
      <defs>
        <linearGradient id="woodKitchen" x1="0" y1="0" x2="1" y2="1">
          <stop offset="0" stop-color="#e9d6b8"/><stop offset="0.45" stop-color="#c98f55"/><stop offset="1" stop-color="#7a4a26"/>
        </linearGradient>
        <linearGradient id="frontBlue" x1="0" y1="0" x2="0" y2="1">
          <stop offset="0" stop-color="#2a78cc"/><stop offset="1" stop-color="#1b3f9a"/>
        </linearGradient>
      </defs>
      <rect x="0" y="140" width="384" height="340" fill="url(#woodKitchen)" role="img" aria-label="Photo of a bright custom kitchen with wooden cabinets and a stone-topped island"/>
      <path d="M0,0 H384 V212 C300,172 170,210 0,168 Z" fill="#5cb947"/>
      <path d="M0,0 H384 V194 C300,154 170,192 0,150 Z" fill="#ffffff"/>
      <path d="M0,450 C90,398 250,432 384,392 L384,542 L0,542 Z" fill="#5cb947"/>
      <path d="M0,470 C100,426 250,452 384,418 L384,542 L0,542 Z" fill="#ffffff"/>
      <path d="M0,476 C100,432 250,458 384,424 L384,542 L0,542 Z" fill="url(#frontBlue)"/>
    </svg>
    <p class="layer tagline">Some Tag Line Goes Here</p>
    <span class="brand-square"></span>
    <p class="layer brand">Hearthline</p>
    <p class="layer cover-phone">403 555 0187</p>
    <p class="layer cover-caption">Custom made kitchens and cabinets company, located in Calgary.</p>
  </section>

  <p class="side-label side-label--front">Front</p>

  <section class="panel inside-left">
    <svg class="panel-art" viewBox="0 0 384 543" width="384" height="543">
      <defs>
        <linearGradient id="whiteKitchen" x1="0" y1="0" x2="1" y2="1">
          <stop offset="0" stop-color="#f4f5f6"/><stop offset="0.6" stop-color="#d9dcdf"/><stop offset="1" stop-color="#b0b4b8"/>
        </linearGradient>
        <linearGradient id="footBlue" x1="0" y1="0" x2="0" y2="1">
          <stop offset="0" stop-color="#2a78cc"/><stop offset="1" stop-color="#1b3f9a"/>
        </linearGradient>
      </defs>
      <rect width="384" height="160" fill="url(#whiteKitchen)" role="img" aria-label="Photo of a white modern kitchen with a dining table and red chairs"/>
      <path d="M0,118 C110,150 260,80 384,110 L384,160 L0,160 Z" fill="#5cb947"/>
      <path d="M0,134 C110,162 260,96 384,124 L384,170 L0,170 Z" fill="#ffffff"/>
      <path d="M0,488 C120,460 260,470 384,476 L384,543 L0,543 Z" fill="#5cb947"/>
      <path d="M0,500 C120,474 260,482 384,486 L384,543 L0,543 Z" fill="url(#footBlue)"/>
      <g transform="translate(14,212)" fill="none" stroke="#3c9a34" stroke-width="2.6">
        <circle cx="12" cy="12" r="11"/><path d="M12 5 V12 L17 15"/>
      </g>
      <g transform="translate(14,284)" fill="none" stroke="#3c9a34" stroke-width="2.2" stroke-linejoin="round">
        <rect x="1" y="10" width="6" height="13"/>
        <path d="M7 11 L12 3 C14 1 16 2 15 6 L14 10 H22 C24 10 25 12 24 14 L22 22 C21 23 20 23 19 23 H7"/>
      </g>
      <path transform="translate(14,408)" d="M12 22 C4 15 0 11 0 6 C0 2 3 0 6 0 C9 0 11 2 12 4 C13 2 15 0 18 0 C21 0 24 2 24 6 C24 11 20 15 12 22 Z" fill="#3c9a34"/>
    </svg>
    <h2 class="layer section-title">Why Choose Us?</h2>
    <h3 class="feature-title" style="top:212px">Availability:</h3>
    <p class="feature-text" style="top:234px">All kitchens are manufactured in a wide range of prices. Searching for a suitable option is easy and fun.</p>
    <h3 class="feature-title" style="top:282px">High quality:</h3>
    <p class="feature-text" style="top:304px">Our company tends to European standards. This involves the careful selection of raw materials, hardware, as well as a neat assembly.</p>
    <p class="feature-text" style="top:356px">High quality of our product is achieved through the use of modern equipment and advanced technology.</p>
    <h3 class="feature-title" style="top:406px">Wide selection</h3>
    <p class="feature-text" style="top:430px">Selling our product includes hundreds of different options: in styles, materials, designs, and colors. All products are easy to use, functional and custom made design.</p>
    <p class="layer footer-domain">www.hearthlinekitchens.com</p>
    <p class="layer footer-phone">403 555 0187</p>
  </section>

  <section class="panel inside-right">
    <svg class="panel-art" viewBox="0 0 386 543" width="386" height="543">
      <defs>
        <linearGradient id="trustGreen" x1="0" y1="0" x2="1" y2="0">
          <stop offset="0" stop-color="#5cb947"/><stop offset="1" stop-color="#74c24c"/>
        </linearGradient>
        <linearGradient id="greyKitchen" x1="0" y1="0" x2="1" y2="1">
          <stop offset="0" stop-color="#eef0f2"/><stop offset="0.5" stop-color="#a9adb2"/><stop offset="1" stop-color="#5e4a3e"/>
        </linearGradient>
      </defs>
      <path d="M0,252 C110,220 250,246 386,206 L386,430 L0,430 Z" fill="#1b3f9a"/>
      <path d="M0,262 C110,232 250,258 386,220 L386,430 L0,430 Z" fill="#ffffff"/>
      <path d="M0,268 C110,238 250,264 386,226 L386,430 L0,430 Z" fill="url(#trustGreen)"/>
      <rect x="0" y="400" width="386" height="143" fill="url(#greyKitchen)" role="img" aria-label="Photo of a modern kitchen with white cabinets and a vase of flowers"/>
      <path d="M0,400 C120,368 250,408 386,378 L386,340 L0,340 Z" fill="url(#trustGreen)"/>
      <path d="M0,420 C120,388 250,428 386,398 L386,408 C250,436 120,398 0,428 Z" fill="#1b3f9a"/>
      <g transform="translate(24,30)" fill="none" stroke="#3c9a34" stroke-width="2.4">
        <circle cx="12" cy="12" r="11"/><path d="M7 14 C9 18 15 18 17 14"/>
        <circle cx="8.5" cy="9" r="1.2" fill="#3c9a34"/><circle cx="15.5" cy="9" r="1.2" fill="#3c9a34"/>
      </g>
      <path transform="translate(24,112)" d="M12 0 L14 6 L18 4 L17 10 L23 9 L20 14 L24 16 L16 18 L13 18 L13 24 L11 24 L11 18 L8 18 L0 16 L4 14 L1 9 L7 10 L6 4 L10 6 Z" fill="#3c9a34"/>
      <path transform="translate(27,194)" d="M8 0 H12 V8 H20 V12 H12 V20 H8 V12 H0 V8 H8 Z" fill="#3c9a34"/>
    </svg>
    <h3 class="feature-title" style="top:26px">Happy Clients:</h3>
    <p class="feature-text" style="top:50px">We are taking into account all the wishes of our customers. We also provide warranty and customer service to bring positive emotions to our clients.</p>
    <h3 class="feature-title" style="top:112px">Proudly Canadian made:</h3>
    <p class="feature-text" style="top:134px">Calgary based production of our products. Custom orders without delays.</p>
    <h3 class="feature-title" style="top:196px">Superior health and safety standards.</h3>
    <h3 class="layer trust-title">Experience You Can Trust</h3>
    <p class="layer trust-text">Lorem ipsum dolor sit amet, consectetur adipiscing elit, sed do eiusmod tempor incididunt ut labore et dolore magna aliqua. Ut enim ad minim veniam, quis nostrud exercitation ullamco laboris nisi ut aliquip ex ea commodo consequat. Duis aute irure dolor in reprehenderit in voluptate velit esse cillum dolore eu fugiat nulla pariatur.</p>
  </section>

  <p class="side-label side-label--back">Back</p>

</main>
</body>
</html>
```